Simple Business Cards for Self-employed Coach

Simple business card with a design that includes the QLT logo.
Using either only the logo color or additional colors that match the logo.

Meridian Guides reach deeply into the past, gathering wisdom from East and West, while still staying current with the frontiers of new discovery in cognitive science, genetics, and other disciplines. see https://www.brightharborpath.example/what-is-integral-coaching/

Target Market(s)

Coaching Clients in Tokyo /Asia; in business organizations, but also outside

Industry/Entity Type

Life Coaching

Contact Information for Business Card

Lukas Brenning
Certified Meridian Guide

3-2-48 Kamiyoshi
Nakarino 164-0392
Tokyo, Japan

Phone: +81 70 4817 5062
E-Mail: lukas.brenning@mailora.example

Font styles to use
Sans Serif

Colors
00a990

Requirements
Must have
• include uploaded logo
• color fitting with QLT logo color
Nice to have
• simple, elegant design
Should not have
• clutter

```html
<!DOCTYPE html>
<html lang="en">
<head>
<meta charset="utf-8">
<title>QLT Business Card</title>
<link href="https://fonts.googleapis.com/css2?family=Source+Sans+3:wght@400;600&display=swap" rel="stylesheet">
<style>
  :root {
    --teal: #0f7a73;
    --ink: #5a5a5a;
    --paper: #ffffff;
    --backdrop: #3b3b3b;
  }
  * { box-sizing: border-box; margin: 0; padding: 0; }
  html, body { width: 1200px; height: 1200px; overflow: hidden; }
  body {
    background: var(--backdrop);
    font-family: "Source Sans 3", sans-serif;
    position: relative;
  }
  .card {
    position: absolute;
    left: 240px;
    width: 722px;
    height: 410px;
  }
  .card-front { top: 167px; background: var(--paper); overflow: hidden; }
  .card-back { top: 623px; background: var(--teal); }

  .brand {
    display: flex;
    align-items: center;
    gap: 14px;
    color: var(--teal);
    font-weight: 600;
    font-size: 54px;
    letter-spacing: 6px;
    line-height: 1;
  }
  .brand-square {
    width: 34px;
    height: 34px;
    background: var(--teal);
  }
  .card-front .brand { position: absolute; left: 430px; top: 62px; }

  .accent-bar {
    position: absolute;
    left: 0; top: 162px;
    width: 14px; height: 53px;
    background: var(--teal);
  }
  .person { position: absolute; left: 34px; top: 161px; }
  .person-name { color: var(--teal); font-size: 29px; font-weight: 400; line-height: 1.15; }
  .person-title { color: var(--ink); font-size: 20px; line-height: 1.3; }

  .contact { position: absolute; left: 34px; top: 234px; list-style: none; }
  .contact li {
    display: flex; align-items: center; gap: 14px;
    color: var(--ink); font-size: 19px; height: 25px;
  }
  .contact svg { width: 21px; height: 18px; fill: var(--teal); }

  .address {
    position: absolute; left: 34px; top: 304px;
    font-style: normal; color: var(--ink); font-size: 19px; line-height: 24px;
  }
  .front-band { position: absolute; left: 0; top: 0; }

  .back-plate {
    position: absolute;
    left: 206px; top: 144px;
    width: 308px; height: 122px;
    background: var(--paper);
    display: flex; align-items: center; justify-content: center;
  }
</style>
</head>
<body>
  <section class="card card-front">
    <div class="brand"><span class="brand-square"></span>QLT</div>

    <div class="accent-bar"></div>
    <div class="person">
      <h1 class="person-name">Lukas Brenning</h1>
      <p class="person-title">Certified Meridian Guide</p>
    </div>

    <ul class="contact">
      <li>
        <svg viewBox="0 0 21 18" aria-hidden="true"><path d="M1 6 C1 2 5 1 10.5 1 S20 2 20 6 L20 7 L15 7 L15 5 L6 5 L6 7 L1 7 Z"/><path d="M4 8 L17 8 L19 17 L2 17 Z"/><circle cx="10.5" cy="12.5" r="2.6" fill="#fff"/></svg>
        +81 70 4817 5062
      </li>
      <li>
        <svg viewBox="0 0 21 18" aria-hidden="true"><path d="M0 2 H21 V16 H0 Z M2 4 L10.5 10 L19 4 V14 L14 9 L13 10 L19 15 H2 L8 10 L7 9 L2 14 Z" fill-rule="evenodd"/></svg>
        lukas.brenning@mailora.example
      </li>
    </ul>

    <address class="address">
      3-2-48 Kamiyoshi<br>
      Nakarino 164-0392<br>
      Tokyo, Japan
    </address>

    <svg class="front-band" width="722" height="410" viewBox="0 0 722 410" aria-hidden="true">
      <polygon points="0,396 360,396 392,382 722,382 722,410 0,410" fill="var(--teal)"/>
    </svg>
  </section>

  <section class="card card-back">
    <div class="back-plate">
      <div class="brand"><span class="brand-square"></span>QLT</div>
    </div>
  </section>
</body>
</html>
```